Copper Kettle Auctions business card design with existing logo

Looking for a sleek and sexy design using our current logo

Contact Information for Business Card

Name, address, email, phone, website. Marcus Delvane 482 Brambleton Road Suite 210C Holtsville NY 11907 Copperkettlebids.net (631)555-0174

```html
<!DOCTYPE html>
<html lang="en">
<head>
<meta charset="utf-8">
<title>Copper Kettle Auctions – Business Card</title>
<link href="https://fonts.googleapis.com/css2?family=Arimo:wght@400;700&display=swap" rel="stylesheet">
<style>
  :root {
    --stage: #1e1e1e;
    --navy: #1b3f7a;
    --red: #d4202b;
    --white: #ffffff;
    --ink: #1c1c1c;
  }
  * { box-sizing: border-box; margin: 0; padding: 0; }
  html, body { width: 1200px; height: 988px; overflow: hidden; background: var(--stage); }
  .stage { position: relative; width: 1200px; height: 988px; }

  .card {
    position: absolute;
    width: 560px; height: 320px;
    border-radius: 18px;
    overflow: hidden;
  }
  .card--front { left: 40px; top: 120px; background: var(--navy); }
  .card--back  { left: 600px; top: 548px; background: var(--white); }

  .brand {
    display: flex; align-items: center; gap: 14px;
    font-family: "Arimo", sans-serif; font-weight: 700;
    text-transform: uppercase; line-height: 1.1;
  }
  .brand-dot { border-radius: 50%; flex: none; }

  /* front side */
  .card--front .brand {
    position: absolute; left: 0; right: 0; top: 0; bottom: 0;
    justify-content: center;
    color: var(--white); font-size: 28px;
  }
  .card--front .brand-dot { width: 56px; height: 56px; background: var(--red); }

  /* back side */
  .card--back .brand {
    position: absolute; left: 36px; top: 40px;
    color: var(--red); font-size: 22px;
  }

  .person { position: absolute; left: 36px; top: 132px; padding-left: 16px; }
  .person::before {
    content: ""; position: absolute; left: 0; top: 4px;
    width: 6px; height: 44px; background: var(--navy);
  }
  .person-name { font-family: "Arimo", sans-serif; font-weight: 700; font-size: 26px; color: var(--red); text-transform: uppercase; }
  .person-role { font-family: "Arimo", sans-serif; font-size: 14px; color: var(--ink); margin-top: 2px; }

  .contact { position: absolute; left: 52px; top: 204px; font-family: "Arimo", sans-serif; font-size: 13px; color: var(--ink); line-height: 1.4; }
  .contact-address { margin-bottom: 6px; }
  .contact-row { display: flex; align-items: center; gap: 7px; }
  .contact-row svg { width: 11px; height: 11px; fill: var(--navy); flex: none; }

  .back-mark {
    position: absolute; right: 70px; top: 80px;
    width: 130px; height: 130px; border-radius: 50%;
    background: var(--navy);
  }
</style>
</head>
<body>
<main class="stage">

  <section class="card card--front" aria-label="Card front">
    <div class="brand">
      <span class="brand-dot"></span>
      <span>Copper Kettle Auctions</span>
    </div>
  </section>

  <section class="card card--back" aria-label="Card back">
    <div class="brand">Copper Kettle Auctions</div>

    <div class="person">
      <div class="person-name">Marcus Delvane</div>
      <div class="person-role">CEO/Founder</div>
    </div>

    <div class="contact">
      <div class="contact-address">482 Brambleton Road Suite<br>210C Holtsville NY 11907</div>
      <div class="contact-row">
        <svg viewBox="0 0 12 12"><path d="M2 1h3l1 3-2 1a7 7 0 0 0 3 3l1-2 3 1v3c0 1-1 1-1 1A10 10 0 0 1 1 2s0-1 1-1z"/></svg>
        (631)555-0174
      </div>
      <div class="contact-row">
        <svg viewBox="0 0 12 12"><path d="M0 2h12v8H0zM1 3l5 4 5-4z" fill-rule="evenodd"/></svg>
        info@copperkettlebids.net
      </div>
      <div class="contact-row">
        <svg viewBox="0 0 12 12"><circle cx="6" cy="6" r="5.5"/></svg>
        www.copperkettlebids.net
      </div>
    </div>

    <div class="back-mark"></div>
  </section>

</main>
</body>
</html>
```